Harlow Vance Law Stationary - logo provided

I need Stationary designed for my Law Firm named Harlow Vance Law.

I have attached the firm's logo and would like that color and logos incorporated into the stationary. I need the stationary to look clean, simple and professional.

I need letterheads, envelopes and business cards designed. I would also like a letterhead version for 5.5 x 8..5 paper size (for handout printing)

Industry/Entity Type

Legal

```html
<!DOCTYPE html>
<html lang="en">
<head>
<meta charset="utf-8">
<title>Harlow Vance Law – Stationery Set</title>
<link href="https://fonts.googleapis.com/css2?family=Cinzel:wght@600&family=Lato:wght@400;700&display=swap" rel="stylesheet">
<style>
  :root{
    --maroon:#7a1f22;
    --gold:#c9a45c;
    --ink:#0c0c0c;
    --paper:#ffffff;
    --frame:#bdbdbd;
    --text:#555555;
    --accent:#d98a2b;
  }
  html,body{margin:0;padding:0;overflow:hidden;}
  body{width:804px;height:1200px;background:var(--paper);position:relative;font-family:"Lato",Arial,sans-serif;}
  .sheet-frame{position:absolute;left:6px;top:6px;right:6px;bottom:6px;border:1px solid var(--frame);}
  .item{position:absolute;box-sizing:border-box;overflow:hidden;}
  .paper{background:var(--paper);border:1px solid #9a9a9a;}
  .dark{background:var(--ink);}

  .brand{display:flex;align-items:center;gap:7px;}
  .brand-mark{width:16px;height:16px;background:var(--maroon);flex:none;}
  .brand-name{font-family:"Cinzel",Georgia,serif;font-weight:600;color:var(--maroon);font-size:14px;letter-spacing:1px;white-space:nowrap;}
  .brand.on-dark .brand-mark{background:var(--gold);}
  .brand.on-dark .brand-name{color:var(--gold);}

  .fine{font-size:5.5px;line-height:8px;color:var(--text);}
  .fine.light{color:#cfcfcf;}

  /* letterhead A4 */
  .letterhead-main{left:59px;top:59px;width:273px;height:424px;}
  .letterhead-main .brand{position:absolute;left:50%;top:196px;transform:translateX(-50%);}

  /* envelope back */
  .envelope-back{left:362px;top:64px;width:402px;height:190px;}
  .envelope-back svg{position:absolute;inset:0;}

  /* envelope front */
  .envelope-front{left:362px;top:268px;width:402px;height:214px;}
  .envelope-front .rule{position:absolute;left:0;right:0;top:10px;height:3px;background:var(--maroon);}
  .envelope-front .fine{position:absolute;left:14px;bottom:12px;width:200px;}
  .envelope-front .brand{position:absolute;right:14px;bottom:12px;}
  .envelope-front .brand-name{font-size:12px;}

  /* half-letter handout */
  .letterhead-handout{left:59px;top:517px;width:273px;height:367px;}
  .letterhead-handout .brand{position:absolute;left:50%;top:160px;transform:translateX(-50%);gap:10px;}
  .letterhead-handout .brand-mark{width:30px;height:30px;}
  .letterhead-handout .brand-name{font-size:18px;}
  .letterhead-handout .fine{position:absolute;left:12px;bottom:10px;}

  /* letterhead letter */
  .letterhead-letter{left:362px;top:517px;width:343px;height:367px;}
  .letterhead-letter .brand{position:absolute;left:50%;top:14px;transform:translateX(-50%);}
  .letterhead-letter .brand-name{font-size:12px;}
  .letterhead-letter .tagline{position:absolute;left:0;right:0;top:36px;text-align:center;}
  .letterhead-letter .footer{position:absolute;left:14px;bottom:14px;}

  /* business card front */
  .card-front{left:59px;top:957px;width:273px;height:190px;}
  .card-front .panel{position:absolute;left:0;top:0;width:168px;height:96px;background:var(--ink);}
  .card-front .firm{position:absolute;left:12px;top:40px;font-family:"Cinzel",Georgia,serif;font-weight:600;font-size:11.5px;color:#ffffff;letter-spacing:0.5px;white-space:nowrap;}
  .card-front .contact{position:absolute;left:178px;top:54px;font-size:6.5px;line-height:9px;color:var(--accent);}
  .card-front .contact strong{font-weight:700;}
  .card-front .address{position:absolute;left:12px;top:108px;}

  /* business card back */
  .card-back{left:362px;top:957px;width:273px;height:190px;}
  .card-back .brand{position:absolute;left:50%;top:50%;transform:translate(-50%,-50%);}
</style>
</head>
<body>
  <div class="sheet-frame"></div>

  <section class="item paper letterhead-main">
    <div class="brand"><span class="brand-mark"></span><span class="brand-name">Harlow Vance Law</span></div>
  </section>

  <section class="item dark envelope-back">
    <svg width="402" height="190" viewBox="0 0 402 190" aria-hidden="true">
      <rect x="3" y="3" width="396" height="184" fill="none" stroke="var(--maroon)" stroke-width="2"/>
      <polyline points="3,3 201,110 399,3" fill="none" stroke="var(--maroon)" stroke-width="3"/>
      <rect x="193" y="122" width="16" height="16" fill="var(--gold)"/>
      <rect x="0" y="184" width="402" height="4" fill="var(--maroon)"/>
    </svg>
  </section>

  <section class="item dark envelope-front">
    <div class="rule"></div>
    <p class="fine light" style="margin:0">Harlow Vance Law | 12 Linden Court, Suite 4, Ashford 2208 | +1 555 0142 | hello@harlowvance.law</p>
    <div class="brand on-dark"><span class="brand-mark"></span><span class="brand-name">Harlow Vance Law</span></div>
  </section>

  <section class="item paper letterhead-handout">
    <div class="brand"><span class="brand-mark"></span><span class="brand-name">Harlow Vance Law</span></div>
    <div class="fine">Harlow Vance Law<br>12 Linden Court, Suite 4<br>Ashford 2208<br>+1 555 0142</div>
  </section>

  <section class="item paper letterhead-letter">
    <div class="brand"><span class="brand-mark"></span><span class="brand-name">Harlow Vance Law</span></div>
    <div class="fine tagline">Attorneys and Counsellors<br>Civil and Family Matters</div>
    <div class="fine footer">12 Linden Court, Suite 4, Ashford 2208 | +1 555 0142<br>hello@harlowvance.law</div>
  </section>

  <section class="item paper card-front">
    <div class="panel"></div>
    <div class="firm">Harlow Vance Law</div>
    <div class="contact"><strong>Elena Marsh</strong><br>Senior Partner<br>+1 555 0142<br>hello@harlowvance.law</div>
    <div class="fine address">12 Linden Court<br>Ashford 2208</div>
  </section>

  <section class="item dark card-back">
    <div class="brand on-dark"><span class="brand-mark"></span><span class="brand-name">Harlow Vance Law</span></div>
  </section>
</body>
</html>
```